Ledge Crafts one page flyer

We need a standard A4 size flyer for a new company called Ledge Crafts. We are a construction material company and sell trims, crown mouldings, baseboards and panelings.
We would like to see the design with the following information:
1. Size: A4
2. Only one front page, no design need to display on back
3. Logo (Ledge Crafts, see the attached EPS file)
4. Slogan: We offer high quality products for competitive prices.
5. Content please see the PDF file
6. The production has 2 category, one called "Crown Moulding", the other is "Wainscoting", Crown Moulding has 5 productions, wainscoting has 2 production(Details see PDF file)
6. We temporary only can provide low resolution images for 7 productions, only the winner will be provided with High Resolution images.
Look and feel
Each slider illustrates characteristics of the customer's brand and the style your logo design should communicate.

```html
<!DOCTYPE html>
<html lang="en">
<head>
<meta charset="utf-8">
<title>Ledge Crafts – Product Flyer</title>
<link rel="stylesheet" href="https://fonts.googleapis.com/css2?family=Josefin+Sans:wght@100;200;400&family=Montserrat:wght@800&family=Quicksand:wght@500;600;700&display=swap">
<style>
  :root {
    --stage: #dcdcdd;
    --paper: #efeff0;
    --paper-light: #f4f4f5;
    --brand-blue: #2450a0;
    --brand-orange: #e8552b;
    --ink-grey: #5c6267;
    --ring-dark: #3a3b3e;
    --white: #ffffff;
  }
  * { margin: 0; padding: 0; box-sizing: border-box; }
  html, body { width: 1200px; height: 1000px; overflow: hidden; }
  body { background: var(--stage); font-family: "Quicksand", sans-serif; }

  .flyer {
    position: absolute; left: 271px; top: 33px;
    width: 658px; height: 934px;
    display: flex;
    box-shadow: 0 6px 18px rgba(0,0,0,.18);
  }

  /* Brand column */
  .brand-column {
    position: relative; width: 197px; height: 100%;
    background: var(--paper-light); overflow: hidden;
  }
  .brand-title, .brand-tagline {
    position: absolute; writing-mode: vertical-rl; transform: rotate(180deg);
    white-space: nowrap; color: var(--ink-grey);
    font-family: "Josefin Sans", sans-serif; text-align: left;
  }
  .brand-title {
    left: 26px; top: 22px; height: 720px;
    font-size: 76px; font-weight: 400; letter-spacing: 2px; line-height: 1;
  }
  .brand-tagline {
    left: 124px; top: 42px; height: 700px;
    font-size: 30px; font-weight: 200; letter-spacing: 5px; line-height: 1;
  }
  .brand-signature {
    position: absolute; left: 28px; bottom: 48px;
    display: flex; align-items: center; gap: 10px;
    font-family: "Quicksand", sans-serif; font-weight: 700;
    font-size: 19px; color: var(--brand-orange);
  }
  .brand-signature .mark { width: 18px; height: 18px; background: var(--brand-orange); }

  /* Blue info column */
  .info-column {
    width: 164px; height: 100%;
    background: var(--brand-blue); color: var(--white);
    text-align: center;
    display: flex; flex-direction: column; align-items: center;
  }
  .section-title {
    margin-top: 26px;
    display: flex; flex-direction: column; align-items: center;
    font-family: "Montserrat", sans-serif; font-weight: 800;
    font-size: 40px; line-height: 50px;
  }
  .section-title span { display: block; height: 50px; }
  .slogan {
    margin-top: 30px; width: 132px;
    font-size: 15px; font-weight: 600; line-height: 1.22;
  }
  .contact {
    margin-top: 26px; font-size: 11.5px; font-weight: 700; line-height: 1.4;
  }
  .info-block { margin-top: 18px; font-size: 10.5px; font-weight: 500; line-height: 1.36; }
  .info-block h3 { font-size: 12px; font-weight: 700; margin-bottom: 5px; letter-spacing: .2px; }

  /* Product column */
  .product-column {
    position: relative; flex: 1; height: 100%;
    background: var(--paper);
  }
  .category-band {
    position: absolute; left: 0; right: 0; height: 46px;
    background: var(--brand-orange); color: var(--white);
    font-family: "Josefin Sans", sans-serif; font-weight: 400;
    font-size: 22px; letter-spacing: .5px;
    display: flex; align-items: center; justify-content: center; padding-top: 4px;
  }
  .band-crown { top: 29px; }
  .band-wainscot { top: 621px; }

  .product { position: absolute; }
  .product-badge { position: absolute; width: 96px; height: 96px; }
  .product-label {
    position: absolute; width: 130px; font-size: 9px; line-height: 1.45;
  }
  .product-name { color: var(--brand-orange); font-weight: 700; }
  .product-size { color: var(--ink-grey); font-weight: 500; }
  .label-right { text-align: left; }
  .label-left { text-align: right; }
</style>
</head>
<body>
<main class="flyer">

  <section class="brand-column">
    <h1 class="brand-title">LEDGE CRAFTS</h1>
    <p class="brand-tagline">FOR ALL TYPES OF PROJECTS</p>
    <div class="brand-signature"><span class="mark"></span>Ledge Crafts</div>
  </section>

  <section class="info-column">
    <h2 class="section-title" aria-label="PRODUTION"><span>P</span><span>R</span><span>O</span><span>D</span><span>U</span><span>T</span><span>I</span><span>O</span><span>N</span></h2>
    <p class="slogan">We offer high quality products for competitive prices.</p>
    <p class="contact">905-555-0142<br>info@ledgecrafts.ca</p>
    <div class="info-block">
      <h3>OFFICE HOURS</h3>
      Mon – Fri : 7:00am – 6.00pm<br>
      Saturdays: 8:00am – 4.00pm<br>
      Sundays: Closed
    </div>
    <div class="info-block">
      <h3>LEDGE CRAFTS</h3>
      Office<br>
      412 Maple Ave, unit 7<br>
      Brookfield, Ontario<br>
      L4B 2K8
    </div>
    <div class="info-block">
      <h3>WAREHOUSE</h3>
      88 Kestrel Dr<br>
      Northvale, ON M3K 1T4<br>
      By Appointment only
    </div>
  </section>

  <section class="product-column">
    <svg width="0" height="0" style="position:absolute">
      <defs>
        <radialGradient id="disc-shade" cx="45%" cy="40%" r="65%">
          <stop offset="0" stop-color="#e4e5e7"/>
          <stop offset="1" stop-color="#c9cacd"/>
        </radialGradient>
        <symbol id="ring" viewBox="0 0 100 100">
          <circle cx="50" cy="50" r="44" fill="none" stroke="var(--brand-orange)" stroke-width="11"/>
          <circle cx="50" cy="50" r="44" fill="none" stroke="var(--brand-blue)" stroke-width="11" stroke-dasharray="69 208" stroke-dashoffset="0"/>
          <circle cx="50" cy="50" r="44" fill="none" stroke="var(--ring-dark)" stroke-width="11" stroke-dasharray="69 208" stroke-dashoffset="-69"/>
          <circle cx="50" cy="50" r="38.5" fill="var(--white)"/>
          <circle cx="50" cy="50" r="34" fill="url(#disc-shade)"/>
        </symbol>
      </defs>
    </svg>

    <div class="category-band band-crown">CROWN MOULDING</div>

    <div class="product" style="left:40px;top:103px">
      <svg class="product-badge" style="transform:rotate(200deg)" role="img" aria-label="Aster 9 crown moulding profile image"><use href="#ring"/></svg>
      <div class="product-label label-right" style="left:112px;top:28px"><div class="product-name">Aster 9 Crown Moulding</div><div class="product-size">8 7/16"x3/4"</div></div>
    </div>

    <div class="product" style="left:157px;top:202px">
      <svg class="product-badge" style="transform:rotate(20deg)" role="img" aria-label="Aster 8 crown moulding profile image"><use href="#ring"/></svg>
      <div class="product-label label-left" style="left:-142px;top:28px"><div class="product-name">Aster 8 Crown Moulding</div><div class="product-size">7 3/4"x3/4"</div></div>
    </div>

    <div class="product" style="left:40px;top:297px">
      <svg class="product-badge" style="transform:rotate(110deg)" role="img" aria-label="Aster 7 crown moulding profile image"><use href="#ring"/></svg>
      <div class="product-label label-right" style="left:112px;top:28px"><div class="product-name">Aster 7 Crown Moulding</div><div class="product-size">6 1/2"x3/4"</div></div>
    </div>

    <div class="product" style="left:157px;top:398px">
      <svg class="product-badge" style="transform:rotate(-70deg)" role="img" aria-label="Linden 8 crown moulding profile image"><use href="#ring"/></svg>
      <div class="product-label label-left" style="left:-142px;top:28px"><div class="product-name">Linden 8 Crown Moulding</div><div class="product-size">7 3/4"x3/4"</div></div>
    </div>

    <div class="product" style="left:40px;top:494px">
      <svg class="product-badge" style="transform:rotate(200deg)" role="img" aria-label="Linden 6 crown moulding profile image"><use href="#ring"/></svg>
      <div class="product-label label-right" style="left:112px;top:28px"><div class="product-name">Linden 6 Crown Moulding</div><div class="product-size">6 1/4"x3/4"</div></div>
    </div>

    <div class="category-band band-wainscot">WAINSCOTING</div>

    <div class="product" style="left:156px;top:701px">
      <svg class="product-badge" style="transform:rotate(110deg)" role="img" aria-label="Colonial chair rail profile image"><use href="#ring"/></svg>
      <div class="product-label label-left" style="left:-142px;top:28px"><div class="product-name">Colonial Chair Rail</div><div class="product-size">3 1/4"x1</div></div>
    </div>

    <div class="product" style="left:45px;top:804px">
      <svg class="product-badge" style="transform:rotate(-160deg)" role="img" aria-label="Colonial panel mould profile image"><use href="#ring"/></svg>
      <div class="product-label label-right" style="left:112px;top:36px"><div class="product-name">Colonial Panel Mould</div><div class="product-size">1 3/4"x5/8"</div></div>
    </div>
  </section>

</main>
</body>
</html>
```